Recreate-branding of doctor office forms

There are forms that need to be re created in vector format following the branding guidelines that are provided. This is a typesetting job not a overly creative job. We are looking for a rebuild on existing forms and have attention to detail.
Updates

Hi All - We would need vector files to be provided in either an EPS format or a PDF. There is a brand identity sheet included with the zip file which was uploaded. We will consider increasing our bid, however, please take the time to look it over. This is a very simple, typeset job and low on the creative. Thanks for your time. TK

Industry/Entity Type

Doctor

```html
<!DOCTYPE html>
<html lang="en">
<head>
<meta charset="utf-8">
<title>Post-Operative Nursing Orders for Extended Stay in Recovery</title>
<link rel="stylesheet" href="https://fonts.googleapis.com/css2?family=Tinos:ital,wght@0,400;0,700;1,400&display=swap">
<style>
  :root {
    --ink: #111111;
    --paper: #ffffff;
  }
  html, body {
    margin: 0;
    padding: 0;
    overflow: hidden;
    background: var(--paper);
  }
  .form-sheet {
    position: relative;
    width: 962px;
    height: 1200px;
    overflow: hidden;
    background: var(--paper);
    color: var(--ink);
    font-family: "Tinos", "Times New Roman", serif;
    font-size: 16px;
    line-height: 20px;
  }
  .form-title {
    position: absolute;
    top: 0;
    left: 0;
    width: 962px;
    margin: 0;
    text-align: center;
    font-size: 27px;
    line-height: 30px;
    font-weight: 700;
  }
  .line {
    position: absolute;
    white-space: nowrap;
  }
  .line.small { font-size: 15px; }
  .label { font-weight: 700; }
  .italic { font-style: italic; }
  .underlined { text-decoration: underline; }
  .blank {
    display: inline-block;
    border-bottom: 1px solid var(--ink);
    height: 14px;
    vertical-align: baseline;
  }
  .check {
    display: inline-block;
    width: 13px;
    height: 13px;
    border: 1px solid var(--ink);
    box-sizing: border-box;
    vertical-align: -1px;
    margin-right: 4px;
    background:
      linear-gradient(45deg, transparent 45%, var(--ink) 45%, var(--ink) 55%, transparent 55%),
      linear-gradient(-45deg, transparent 45%, var(--ink) 45%, var(--ink) 55%, transparent 55%);
  }
  .check.mini { width: 9px; height: 9px; }
  .rule {
    position: absolute;
    height: 0;
    border-top: 1px solid var(--ink);
  }
</style>
</head>
<body>
<main class="form-sheet">
  <h1 class="form-title">Post-Operative Nursing Orders for Extended Stay in Recovery</h1>

  <div class="line small" style="top:32px;left:3px"><span class="label">Patient Name/ID #:</span><span class="blank" style="width:290px"></span></div>

  <div class="line" style="top:51px;left:3px"><span class="label">Vital Signs:</span> Record every 15 minutes x first hour, every 30 minutes x the following hour, then every 60 minutes, if stable.</div>
  <div class="line" style="top:72px;left:3px">Notify surgeon immediately if:</div>
  <div class="line" style="top:93px;left:113px"><span class="label">a.</span>&nbsp;&nbsp;&nbsp;SBP &gt; 180, &lt; 90</div>
  <div class="line" style="top:116px;left:113px"><span class="label">b.</span>&nbsp;&nbsp;&nbsp;DBP &gt;125, &lt; 55</div>
  <div class="line" style="top:138px;left:113px"><span class="label">c.</span>&nbsp;&nbsp;&nbsp;HR &gt; 125 for longer than 5 minutes, &lt; 50</div>
  <div class="line" style="top:161px;left:113px"><span class="label">d.</span>&nbsp;&nbsp;&nbsp;SpO2 &lt; 94%</div>
  <div class="line" style="top:183px;left:113px"><span class="label">e.</span>&nbsp;&nbsp;&nbsp;Temp &gt; 101.5 degrees F</div>

  <div class="line" style="top:203px;left:3px"><span class="label">Nursing:</span> a.) Elevate head of bed &gt;30 degrees</div>
  <div class="line" style="top:228px;left:74px">b.) O2 via nasal canula at 5 L/min, wean as tolerated to room air keeping sats &gt;94%</div>
  <div class="line" style="top:250px;left:77px">c.) Routine surgical site checks for excess bleeding or secretions. Gently suction mouth/nose, as needed.</div>
  <div class="line" style="top:274px;left:74px">d.) Ice pack to surgical sites 20 minutes on, 20 minutes off with towel to cover pack to prevent injury.</div>
  <div class="line" style="top:296px;left:66px">e.) Activity: Pt is high risk to fall. Have pt ambulate with assistance until time of discharge. Educate family/escort to</div>
  <div class="line" style="top:317px;left:136px">continue to assist patient after discharge.</div>

  <div class="line" style="top:342px;left:3px"><span class="check"></span> Keep IV at TKO. Prior to discharge, heparin lock IV</div>
  <div class="line" style="top:376px;left:3px"><span class="check"></span> Sequential Compression Devices to bilateral lower extremities, ok to discontinue once ambulatory. Keep Thrombo Embolic</div>
  <div class="line" style="top:399px;left:22px">Deterrent Hose on until time of patient discharge.</div>

  <div class="line label" style="top:425px;left:5px">Medications (standard adult dosing listed, weight adjusted for pediatrics cases per doctor):</div>
  <div class="line" style="top:453px;left:3px"><span class="check"></span> <span class="label">Dexamethasone-</span> <span class="check"></span> 6mg IV Q6H <span class="check"></span> 8mg IV Q6H <span class="check"></span> Other:<span class="blank" style="width:120px"></span></div>
  <div class="line" style="top:488px;left:3px"><span class="check"></span> <span class="label">Cefazolin</span> - <span class="check"></span> 500mg IV Q6H <span class="check"></span> 1 gram IV Q6H <span class="check"></span> Other:<span class="blank" style="width:120px"></span></div>
  <div class="line" style="top:518px;left:136px"><span class="italic">If allergic to Cefazolin/PCN</span>, give <span class="label">Clindamycin</span> <span class="check"></span> 600mg IV Q6H <span class="check"></span> 900mg IV Q8H <span class="check"></span> Other: <span class="blank" style="width:80px"></span></div>

  <div class="line label" style="top:543px;left:3px">Pain:</div>
  <div class="line" style="top:573px;left:3px"><span class="check"></span> <span class="label">Ketorolac</span> 30mg IV q 4-6 hrs prn pain, x 2 doses (pt to receive no more than 60 mg q 12 hrs).</div>
  <div class="line" style="top:608px;left:3px"><span class="check"></span> <span class="label">Fentanyl</span> 25-100 mcg IV push q 5-10 minutes prn pain. Titrate to effect. Do not exceed 100mcg.</div>
  <div class="line" style="top:642px;left:3px"><span class="check"></span> <span class="label">Morphine</span> 1-2 mg IV q 15 minutes prn pain. Titrate to effect. Do not exceed 4mg.</div>
  <div class="line" style="top:677px;left:3px"><span class="check"></span> <span class="label">Meperidine</span> 25-75 mg IV q 15 minutes prn pain. Titrate to effect. Do NOT exceed 100 mg.</div>
  <div class="line" style="top:708px;left:3px"><span class="check"></span> &nbsp;<span class="label">Other</span>: <span class="blank" style="width:180px"></span></div>

  <div class="line label" style="top:732px;left:3px">Nausea:</div>
  <div class="line" style="top:761px;left:3px"><span class="check"></span> <span class="label">Ondansetron</span> &nbsp;4mg IV q 2-4 hrs prn nausea/vomiting.</div>
  <div class="line" style="top:795px;left:3px"><span class="check"></span> <span class="label">Promethazine</span> <span class="check"></span>12.5 mg <span class="check"></span> 25mg IV q 4 hrs prn nausea/vomiting. SLOW IV push.</div>
  <div class="line" style="top:818px;left:3px"><span class="check mini"></span> Once pt has met discharge criteria protocol, pt may be discharged to the care of family/escort.</div>
  <div class="line" style="top:840px;left:3px"><span class="check mini"></span> Schedule patient for follow-up appointment:</div>
  <div class="line" style="top:871px;left:3px"><span class="check"></span> Next Day <span class="check"></span> 7-10 days &nbsp;<span class="check"></span> 2 weeks <span class="check"></span> Other <span class="blank" style="width:48px"></span></div>

  <div class="line small" style="top:902px;left:8px"><span class="label">Home Rx:</span> <span class="check"></span> Dexamethasone Elixer 0.5mg/5ml- Tapering Dose</div>
  <div class="line small" style="top:924px;left:3px">Dispense 320 cc. Take 20 cc PO QID for two days,</div>
  <div class="line small" style="top:944px;left:3px">20cc PO BID for one day, 20cc PO for one day then d/c.&nbsp;&nbsp; Renewal:0</div>

  <div class="line small" style="top:902px;left:542px"><span class="check"></span> Hydrocodone/APAP Elixer 2.5mg/5cc</div>
  <div class="line small" style="top:924px;left:542px">Dispense 8oz. Take one tbsp (15cc) Q4-6h prn pain.</div>
  <div class="line small" style="top:944px;left:610px">Renewal: <span class="underlined">1</span></div>

  <div class="line small" style="top:971px;left:3px"><span class="check"></span> Ibuprofen Suspension 100mg/5cc.</div>
  <div class="line small" style="top:992px;left:17px">Dispense 8oz. Take 2-6 tsp PO Q6H prn</div>
  <div class="line small" style="top:1013px;left:17px">Renewal: <span class="underlined">2</span></div>

  <div class="line small" style="top:971px;left:542px"><span class="check"></span> Cephalexin Suspension 250mg/5cc</div>
  <div class="line small" style="top:992px;left:542px">Dispense 1 week supply. Take 500mg PO Q6H until gone.</div>
  <div class="line small" style="top:1013px;left:542px">Renewal: <span class="underlined">0</span></div>

  <div class="line small" style="top:1040px;left:3px"><span class="check"></span> Acetaminophen with Codeine Elixer 12mg/5cc</div>
  <div class="line small" style="top:1067px;left:3px">Dispense 8oz. Take 1-2 tsp (5cc) PO Q4-6H prn pain</div>
  <div class="line small" style="top:1087px;left:3px">Caution: Sedation &nbsp;&nbsp; Renewal: 0</div>

  <div class="line small" style="top:1040px;left:542px"><span class="check"></span> See OMS Medication Scripts</div>
  <div class="line small" style="top:1067px;left:542px"><span class="check"></span> Chlorhexidine Rinse</div>

  <div class="line" style="top:1117px;left:3px"><span class="check"></span> Other:</div>
  <div class="rule" style="top:1134px;left:68px;width:882px"></div>
  <div class="line small label" style="top:1138px;left:3px">Special Instructions:</div>
  <div class="rule" style="top:1172px;left:0;width:860px"></div>
  <div class="line" style="top:1179px;left:3px"><span class="label">Doctor's Signature:</span><span class="blank" style="width:168px"></span></div>
  <div class="line" style="top:1179px;left:474px">Date/Time:<span class="blank" style="width:152px"></span></div>
</main>
</body>
</html>
```